Pest Control Company needs business card!

Hi there, we need a business card designed for our new Pest Control Company. Ideally this card will be simple, yet feel elegant and high end. We want to use the colours Orange, Black and White. Please see our attached logo for the exact colours.

Business card details:

Phone - 0461 275 804
Name - Gavin Holloway
Email - Info@steadfastverminguard.com.au

We would also like to include the following list with dot points:

SERVICES / INSPECTIONS

Termites, Wood Borers, Ants, Cockroaches, Spiders, Fleas, Mice, Rats, Bed Bugs, & More!

```html
<!DOCTYPE html>
<html lang="en">
<head>
<meta charset="utf-8">
<title>Steadfast Vermin Guard – Business Card</title>
<link rel="stylesheet" href="https://fonts.googleapis.com/css2?family=Montserrat:wght@400;600;700;800&display=swap">
<style>
  :root {
    --orange: #f47f1f;
    --orange-deep: #d9691a;
    --black: #000000;
    --white: #ffffff;
    --ink: #111111;
    --backdrop: #2b201a;
    --silhouette-soft: #dcdcdc;
  }
  * { box-sizing: border-box; margin: 0; padding: 0; }
  html, body {
    width: 970px; height: 1200px; overflow: hidden;
    background: var(--backdrop);
    font-family: "Montserrat", Arial, sans-serif;
  }
  .canvas { position: relative; width: 970px; height: 1200px; }

  .card {
    position: absolute; left: 99px; width: 773px; height: 500px;
    overflow: hidden; background: var(--white);
  }
  .card--front { top: 73px; }
  .card--back  { top: 627px; }
  .card__split { position: absolute; inset: 0; width: 773px; height: 500px; }

  /* Front */
  .brand-name {
    position: absolute; left: 50px; top: 300px; width: 230px;
    color: var(--orange); font-weight: 800; font-size: 38px;
    line-height: 1.1; text-transform: uppercase; text-align: center;
  }
  .brand-mark {
    position: absolute; left: 130px; top: 235px; width: 40px; height: 40px;
    border-radius: 50%; background: var(--orange);
  }
  .contact { position: absolute; right: 32px; text-align: right; color: var(--ink); white-space: nowrap; }
  .contact__icon {
    position: absolute; right: 31px; width: 46px; height: 46px;
    border-radius: 50%; background: var(--orange);
    display: flex; align-items: center; justify-content: center;
  }
  .contact__icon svg { width: 24px; height: 24px; }
  .contact--name  { top: 155px; font-size: 22px; font-weight: 700; }
  .contact--phone { top: 285px; font-size: 23px; font-weight: 400; letter-spacing: 0.5px; }
  .contact--email { top: 415px; font-size: 23px; font-weight: 400; }
  .icon--person { top: 89px; }
  .icon--phone  { top: 219px; }
  .icon--mail   { top: 349px; }

  /* Back */
  .pest-illustration {
    position: absolute; left: 0; top: 0; width: 416px; height: 310px;
    background: linear-gradient(160deg, var(--white) 10%, var(--silhouette-soft));
    clip-path: polygon(0 0, 286px 0, 416px 310px, 0 310px);
  }
  .mascot-illustration {
    position: absolute; left: 385px; top: 15px; width: 350px; height: 330px;
    border-radius: 50%;
    background: radial-gradient(ellipse at 50% 52%, var(--orange) 0%, var(--orange-deep) 50%, rgba(0,0,0,0) 71%);
  }
  .service-list {
    position: absolute; top: 330px; list-style: none;
    font-size: 25.5px; line-height: 31px; color: var(--ink);
  }
  .service-list--left  { left: 32px; }
  .service-list--right { left: 278px; }
  .services-title {
    position: absolute; left: 492px; top: 379px;
    color: var(--orange); font-weight: 700; font-size: 25.5px;
    line-height: 30px; text-transform: uppercase; white-space: nowrap;
  }
</style>
</head>
<body>
<main class="canvas">

  <section class="card card--front" aria-label="Business card front">
    <svg class="card__split" viewBox="0 0 773 500" aria-hidden="true">
      <polygon points="0,0 491,0 277,500 0,500" fill="var(--black)"/>
    </svg>
    <span class="brand-mark" aria-hidden="true"></span>
    <h1 class="brand-name">Steadfast Vermin Guard</h1>

    <span class="contact__icon icon--person" aria-hidden="true">
      <svg viewBox="0 0 24 24" fill="none" stroke="#fff" stroke-width="1.6">
        <circle cx="12" cy="8" r="4"/><path d="M4 21c0-4.5 3.5-7 8-7s8 2.5 8 7z"/>
      </svg>
    </span>
    <p class="contact contact--name">Gavin Holloway</p>

    <span class="contact__icon icon--phone" aria-hidden="true">
      <svg viewBox="0 0 24 24" fill="none" stroke="#fff" stroke-width="1.6" stroke-linejoin="round">
        <path d="M5 3h4l2 5-2.5 1.5a11 11 0 0 0 6 6L16 13l5 2v4a2 2 0 0 1-2 2A16 16 0 0 1 3 5a2 2 0 0 1 2-2z"/>
      </svg>
    </span>
    <p class="contact contact--phone">0461 275 804</p>

    <span class="contact__icon icon--mail" aria-hidden="true">
      <svg viewBox="0 0 24 24" fill="none" stroke="#fff" stroke-width="1.6" stroke-linejoin="round">
        <rect x="3" y="6" width="18" height="12"/><path d="M3 6l9 7 9-7M3 18l7-6M21 18l-7-6"/>
      </svg>
    </span>
    <p class="contact contact--email">Info@steadfastverminguard.com.au</p>
  </section>

  <section class="card card--back" aria-label="Business card back">
    <svg class="card__split" viewBox="0 0 773 500" aria-hidden="true">
      <polygon points="286,0 773,0 773,500 496,500" fill="var(--black)"/>
    </svg>
    <div class="pest-illustration" role="img" aria-label="Black silhouettes of a rat, ants, cockroaches, beetles, flies and bugs swarming"></div>
    <div class="mascot-illustration" role="img" aria-label="Orange cartoon bug mascot running in alarm"></div>

    <ul class="service-list service-list--left">
      <li>Termites</li><li>Wood Borers</li><li>Ants</li><li>Cockroaches</li><li>Spiders</li>
    </ul>
    <ul class="service-list service-list--right">
      <li>Fleas</li><li>Mice</li><li>Rats</li><li>Bed Bugs</li><li>&amp; More!</li>
    </ul>
    <h2 class="services-title">Services /<br>Inspections</h2>
  </section>

</main>
</body>
</html>
```